Velmoria - 3D medical animations and high end visual content

Our company creates high end visual content and animations for medical global companies.
Our website - www.velmoria-studio.example
We would like to have an amazing business card for our CEO that he can use in the following exhebitions he is going to attend.
It is very important that the design will be memorable and diffrent. It has to reflect our brand design (you can have it from our website)
We would like to transmit innovation, prestige, luxury, aesthetics.
The card has to be Double Sided

Target Market(s)

Marketing managers in medical global companys

Industry/Entity Type

It Company

Contact Information for Business Card

Requirements
Nice to have
• It is very important that the design will be memorable and diffrent. It has to reflect our brand design (you can have it from our website)

```html
<!DOCTYPE html>
<html lang="en">
<head>
<meta charset="utf-8">
<title>Velmoria Business Card</title>
<link rel="stylesheet" href="https://fonts.googleapis.com/css2?family=Montserrat:wght@400;500;600;700&display=swap">
<style>
  :root {
    --backdrop: #2c2c2e;
    --ink: #0a0a0a;
    --paper: #ffffff;
    --teal: #0f8ea8;
    --gold: #f5c518;
    --rule-light: #bdbdbd;
    --rule-dark: #555555;
  }
  html, body {
    margin: 0;
    padding: 0;
    width: 1200px;
    height: 900px;
    overflow: hidden;
    background: var(--backdrop);
    font-family: "Montserrat", Arial, sans-serif;
  }
  .canvas {
    position: relative;
    width: 1200px;
    height: 900px;
  }
  .card {
    position: absolute;
    width: 680px;
    height: 388px;
    border-radius: 22px;
    overflow: hidden;
    box-shadow: 0 14px 30px rgba(0,0,0,0.45);
  }
  .card svg { display: block; }
  .card--front { left: 190px; top: 48px; background: var(--ink); }
  .card--back  { left: 330px; top: 464px; background: var(--paper); }
  .wordmark {
    font-family: "Montserrat", Arial, sans-serif;
    font-weight: 600;
    font-size: 40px;
    letter-spacing: 3px;
  }
  .wordmark--light { fill: var(--paper); }
  .wordmark--dark { fill: var(--ink); }
  .contact-name {
    font-weight: 700;
    font-size: 21px;
    letter-spacing: 3px;
    fill: var(--teal);
  }
  .contact-role { font-weight: 500; font-size: 14px; fill: var(--paper); }
  .contact-line { font-weight: 400; font-size: 14px; fill: var(--paper); }
  .contact-accent { fill: var(--teal); }
  .icon { fill: none; stroke: var(--gold); stroke-width: 1.6; }
</style>
</head>
<body>
<main class="canvas">

  <!-- Front side -->
  <section class="card card--front" aria-label="Card front">
    <svg width="680" height="388" viewBox="0 0 680 388">
      <defs>
        <clipPath id="front-arc-top">
          <polygon points="0,0 190,0 190,60 95,82 0,150"/>
        </clipPath>
        <clipPath id="front-arc-bottom">
          <polygon points="190,388 420,388 420,130 310,175 190,330"/>
        </clipPath>
      </defs>
      <rect class="card-base" width="680" height="388" fill="var(--ink)"/>
      <g fill="var(--teal)">
        <circle cx="170" cy="200" r="180" clip-path="url(#front-arc-top)"/>
        <circle cx="170" cy="200" r="180" clip-path="url(#front-arc-bottom)"/>
      </g>
      <circle class="front-disc" cx="150" cy="212" r="165" fill="var(--paper)"/>
      <text class="wordmark wordmark--light" x="505" y="212" text-anchor="middle">VELMORIA</text>
      <line class="wordmark-rule" x1="365" y1="232" x2="645" y2="232" stroke="var(--rule-light)" stroke-width="1"/>
    </svg>
  </section>

  <!-- Back side -->
  <section class="card card--back" aria-label="Card back">
    <svg width="680" height="388" viewBox="0 0 680 388">
      <defs>
        <clipPath id="back-ring-left">
          <rect x="0" y="0" width="540" height="388"/>
        </clipPath>
        <clipPath id="back-arc-top">
          <polygon points="420,0 680,0 680,120 560,60 420,40"/>
        </clipPath>
        <clipPath id="back-arc-bottom">
          <polygon points="520,388 680,388 680,200 610,230 520,360"/>
        </clipPath>
      </defs>
      <rect class="card-base" width="680" height="388" fill="var(--paper)"/>
      <text class="wordmark wordmark--dark" x="175" y="222" text-anchor="middle">VELMORIA</text>
      <line class="wordmark-rule" x1="40" y1="242" x2="310" y2="242" stroke="var(--rule-dark)" stroke-width="1"/>

      <circle class="gold-ring" cx="556" cy="196" r="190" fill="none" stroke="var(--gold)" stroke-width="4" clip-path="url(#back-ring-left)"/>
      <g fill="var(--teal)">
        <circle cx="578" cy="186" r="186" clip-path="url(#back-arc-top)"/>
        <circle cx="578" cy="186" r="186" clip-path="url(#back-arc-bottom)"/>
      </g>
      <circle class="contact-disc" cx="562" cy="198" r="176" fill="var(--ink)"/>

      <g class="contact-block" text-anchor="end">
        <text class="contact-name" x="640" y="110">EITAN MARLOW</text>
        <text class="contact-role" x="640" y="132">Founder &amp; CEO</text>
        <text class="contact-line" x="622" y="170">+972-52-4417308</text>
        <text class="contact-line" x="622" y="194">+972-77-6032915</text>
        <text class="contact-line" x="622" y="228">eitan@velmoria-studio.example</text>
        <text class="contact-line" x="622" y="252">www.<tspan class="contact-accent">velmoria-studio</tspan>.example</text>
      </g>

      <g class="contact-icons">
        <rect class="icon" x="633" y="156" width="9" height="15" rx="2"/>
        <path class="icon" d="M632 184 q2 -3 4 0 l1 3 q-1 2 1 4 q2 2 4 1 l3 1 q3 2 0 4 q-6 2 -11 -4 q-4 -5 -2 -9z"/>
        <g class="icon">
          <rect x="631" y="217" width="14" height="10" rx="1"/>
          <path d="M631 218 l7 5 l7 -5"/>
        </g>
        <g class="icon">
          <circle cx="638" cy="247" r="7"/>
          <ellipse cx="638" cy="247" rx="3" ry="7"/>
          <path d="M631 247 h14"/>
        </g>
      </g>
    </svg>
  </section>

</main>
</body>
</html>
```